Recruitment Package Design for Healthcare Organization

We need a brochure designed that matches the design of our website and logo. The focus of the brochure is to provide information about our organization and region to prospective physicians looking to join our team. I have the content already put together, but would like some imagery of local geography/activities to be incorporated into the design. I have attached the content document as well as an example we are wanting to model ours after.

Our website is: https://brightmarrowcare.ca/

Target Market(s)

Prospective physicians

Industry/Entity Type

Healthcare

Requirements
Must have
• Local imagery which I have attached.

```html
<!DOCTYPE html>
<html lang="en">
<head>
<meta charset="utf-8">
<title>Bright Marrow Care – Physician Recruitment Brochure</title>
<link href="https://fonts.googleapis.com/css2?family=Montserrat:ital,wght@0,300;0,400;0,500;0,600;1,300&display=swap" rel="stylesheet">
<style>
:root{
  --bg:#e4e4e6;
  --teal:#36d3dc;
  --teal-soft:#9fe9ec;
  --teal-pale:#d6f6f7;
  --page-left:#f1f1f1;
  --page-right:#fbfbfb;
  --ink:#333;
  --ink-soft:#555;
  --rule:#8a8a8a;
  --tab:#6b6b6b;
  --plus-grey:#c4c4c4;
}
*{box-sizing:border-box;margin:0;padding:0}
html,body{width:1200px;height:3937px;overflow:hidden}
body{background:var(--bg);font-family:"Montserrat",sans-serif;color:var(--ink);position:relative}
.spread{position:absolute;left:120px;width:960px;height:720px;display:flex;box-shadow:0 6px 18px rgba(0,0,0,.12)}
.spread--cover{top:110px}.spread--two{top:1050px}.spread--three{top:2010px}.spread--four{top:2970px}
.page{position:relative;width:480px;height:720px;overflow:hidden}
.page--left{background:var(--page-left)}
.page--right{background:var(--page-right)}
.corner{position:absolute;background:var(--teal)}
.corner--tl{left:0;top:0;width:120px;height:120px;clip-path:polygon(0 0,100% 0,0 100%)}
.corner--br{right:0;bottom:0;width:120px;height:120px;clip-path:polygon(100% 0,100% 100%,0 100%)}
.corner--tl-pale{background:linear-gradient(135deg,var(--teal-soft),var(--teal-pale))}
.page-tab{position:absolute;right:34px;bottom:34px;width:56px;height:56px;background:var(--tab);color:#fff;font-size:16px;display:flex;align-items:center;justify-content:center}
.brand{color:var(--teal);font-weight:400;line-height:1}
.brand-mark{display:flex;align-items:center;gap:12px}
.brand-dot{width:34px;height:34px;border:2px solid #9a9a9a;border-radius:50%;flex:none}
.brand--inside{position:absolute;left:0;right:0;top:42px;display:flex;justify-content:center}
.brand--inside .brand{font-size:28px}
.rule{position:absolute;left:64px;right:48px;height:1px;background:var(--rule)}
.heading{font-size:12px;font-weight:500;text-align:center;color:var(--ink)}
.body{font-size:7.3px;line-height:1.42;color:var(--ink);text-align:justify}
.body p{margin-bottom:7px}
.plus{position:absolute;width:40px;height:40px}
.plus::before,.plus::after{content:"";position:absolute;background:var(--teal-soft)}
.plus::before{left:35%;top:0;width:30%;height:100%}
.plus::after{top:35%;left:0;height:30%;width:100%}
.plus--grey::before,.plus--grey::after{background:var(--plus-grey)}
.plus--teal::before,.plus--teal::after{background:var(--teal)}
.diamond{position:absolute;transform:rotate(45deg);overflow:hidden}
.diamond-frame{position:absolute;transform:rotate(45deg);border:2px solid var(--teal);border-radius:14px}
/* cover back */
.cover-band{position:absolute;inset:0;background:linear-gradient(45deg,var(--teal-soft),var(--teal-pale) 60%,#fff);clip-path:polygon(0 64%,0 40%,62% 0,100% 0,100% 6%)}
.cover-heart{left:112px;top:224px;width:250px;height:250px;border-radius:44px;background:radial-gradient(circle at 50% 45%,#f5c77a 0,#3a8fd0 35%,#0c3a78 75%)}
.cover-back-brand{position:absolute;left:0;right:0;top:596px;display:flex;justify-content:center}
.cover-back-brand .brand{font-size:26px}
.cover-url{position:absolute;left:0;right:0;top:656px;text-align:center;font-size:11px;color:var(--ink-soft)}
/* cover front */
.cover-front-brand{position:absolute;left:84px;top:42px;display:flex;align-items:center;gap:16px}
.cover-front-brand .brand{font-size:44px}
.cover-front-brand .brand span{display:block;font-size:18px;letter-spacing:4px;margin-top:6px}
.img-trail{left:140px;top:206px;width:210px;height:210px;border-radius:12px;background:linear-gradient(135deg,#3b6a2e,#8bb07a 45%,#c89a7a 70%,#8a6a55)}
.frame-trail{left:120px;top:186px;width:250px;height:250px}
.img-city{left:186px;top:420px;width:152px;height:152px;border-radius:10px;background:linear-gradient(180deg,#8fb3d8,#5d89a8 40%,#6f7d5c 75%,#4a5a3e)}
.taglines{position:absolute;left:0;right:0;top:622px;display:flex;justify-content:center;gap:18px;font-size:15px;text-align:center;color:var(--ink);font-weight:500}
.taglines span{display:block;color:var(--teal);font-weight:400}
.tag-divider{width:1px;background:#999}
/* inner pages */
.ceo-text{position:absolute;left:64px;right:48px;top:206px}
.signoff{position:absolute;left:64px;right:48px;top:560px;display:flex;justify-content:space-between;font-size:7.3px}
.signoff .url{display:inline-block;margin-top:6px;background:var(--teal);color:#133;padding:2px 8px;border-radius:8px;font-size:8px}
.signoff .name{text-align:right}
.signoff .name strong{display:block;font-size:11px;font-weight:500;margin-top:6px}
.about-text{position:absolute;left:64px;right:56px;top:170px}
.body--loose{font-size:7.6px;line-height:2.05}
.frame-chair{left:90px;top:485px;width:170px;height:170px}
.img-chair{left:107px;top:502px;width:136px;height:136px;border-radius:8px;background:linear-gradient(135deg,#f5c35a,#d88a2a 45%,#6a3a1a 80%)}
.mission-text{position:absolute;left:64px;right:48px;top:142px}
.mission-text .heading{margin:8px 0 10px}
.body--italic{font-style:italic;font-weight:300}
.testi-text{position:absolute;left:64px;right:50px;top:100px}
.testi-text .gap{height:22px}
.region-text{position:absolute;left:64px;right:46px;top:140px}
.region-text .heading{margin:6px 0 8px}
.todo{display:grid;grid-template-columns:1fr 1fr;gap:6px 18px;font-size:7.3px;padding:0 18px}
.lists{position:absolute;inset:0}
.list-block{position:absolute;width:200px}
.list-block h3{font-size:11px;font-weight:500;margin:0 0 6px 20px}
.list-block ul{list-style:none;font-size:7.2px;line-height:1.45;margin-left:20px}
.list-block li::before{content:"• "}
.list-block .plus{left:-6px;top:-14px;width:26px;height:26px}
.frame-ski{left:150px;top:445px;width:170px;height:170px}
.img-ski{left:143px;top:457px;width:146px;height:146px;border-radius:10px;background:linear-gradient(135deg,#e9f1f8,#b8cde0 45%,#5b7fa0 80%,#2f4a66)}
</style>
</head>
<body>

<section class="spread spread--cover">
  <div class="page page--left">
    <div class="cover-band"></div>
    <div class="diamond cover-heart" role="img" aria-label="Glowing heart held between open hands"></div>
    <div class="cover-back-brand"><div class="brand-mark"><span class="brand-dot"></span><span class="brand">Bright Marrow Care</span></div></div>
    <p class="cover-url">www.brightmarrowcare.ca</p>
    <div class="corner corner--br"></div>
  </div>
  <div class="page page--right">
    <div class="corner corner--tl corner--tl-pale" style="width:110px;height:110px"></div>
    <div class="cover-front-brand"><span class="brand-dot" style="width:54px;height:54px"></span><div class="brand">Bright Marrow<span>CARE</span></div></div>
    <div class="plus plus--grey" style="left:96px;top:206px;width:34px;height:34px"></div>
    <div class="plus" style="left:40px;top:248px;width:56px;height:56px"></div>
    <div class="plus" style="left:92px;top:418px;width:50px;height:50px"></div>
    <div class="plus plus--grey" style="left:364px;top:424px;width:36px;height:36px"></div>
    <div class="diamond-frame frame-trail"></div>
    <div class="diamond img-trail" role="img" aria-label="Cyclists riding a wooden trestle trail through forest"></div>
    <div class="diamond img-city" role="img" aria-label="Lakeside city skyline with mountains behind"></div>
    <div class="taglines">
      <div>YOUR PARTNER<span>IN HEALTH.</span></div>
      <div class="tag-divider"></div>
      <div>YOUR PARTNER<span>IN LIFE.</span></div>
    </div>
    <div class="corner corner--br" style="width:100px;height:100px"></div>
  </div>
</section>

<section class="spread spread--two">
  <div class="page page--left">
    <div class="corner corner--tl"></div>
    <div class="brand--inside"><div class="brand-mark"><span class="brand-dot"></span><span class="brand">Bright Marrow Care</span></div></div>
    <div class="rule" style="top:148px"></div>
    <h2 class="heading" style="position:absolute;left:0;right:0;top:168px;padding-left:16px">CEO Message</h2>
    <div class="ceo-text body">
      <p>Thank you for your interest in Bright Marrow Care – whether you are a recent graduate looking to establish your practice or a veteran physician looking for a change, I am confident you can find your healthcare home here. It is my privilege to helm an organization that is truly committed to creating the best possible experiences and outcomes for our patients and the communities we serve. As the Okanagan's population has boomed over the last decade, there is even greater need to provide residents with access to essential healthcare services. Our time-tested and sustainable operating model has enabled us to not only survive, but thrive through the many challenges that the past 5 years have presented the healthcare industry.</p>
      <p>Founded in 2016, Bright Marrow Care is an established organization with a strong reputation in the communities we serve. From a business perspective, our revenue is healthy and our trajectory is positive.</p>
      <p>The numbers back this up:</p>
      <p>• In fiscal year 2024, Bright Marrow Care provided more than 163,000 patient visits.</p>
      <p>• Fiscal year 2024 gross annual revenue was $3.45 million, representing a 70% year-over-year growth rate from fiscal year 2023.</p>
      <p>• Year-to-date gross revenue is up 3.8%, over the same period last year.</p>
      <p>Bright Marrow Care is led by an experienced and well-balanced leadership team which includes our medical directors, management team and senior leadership team. This unique combination of backgrounds and experiences helps to inform and shape the decisions and direction of the organization.</p>
      <p>If you would like to learn more about how we continue to keep our commitment of "creating exceptional experiences for every patient, every time",</p>
    </div>
    <div class="signoff">
      <div>I encourage you to visit our website at<br><span class="url">www.brightmarrowcare.ca</span></div>
      <div class="name">Sincerely,<strong>Tobin Raske, CEO</strong></div>
    </div>
    <div class="corner corner--br"></div>
    <div class="page-tab">Pg 2</div>
  </div>
  <div class="page page--right">
    <div class="corner corner--tl"></div>
    <h2 class="heading" style="position:absolute;left:0;right:0;top:112px">About Tobin and Marielle Raske</h2>
    <div class="rule" style="top:140px"></div>
    <div class="about-text body body--loose">
      Prior to working in the healthcare industry, Tobin spent 15 years in operations and human resources management for a large communications company. After shifting focus to the healthcare industry 9 years ago, he took on the role of Operations Manager for a pharmacy chain and was tasked with getting our first two locations built, staffed and operational. These clinics, Ridgeview Medical Clinic and Heron Bay Medical Clinic, pre-dated the Bright Marrow Care name, but were the foundation upon which the organization was built. In 2020, along with his wife Marielle, a registered nurse and soon-to-be business partner, they purchased the two clinics and Bright Marrow Care was born. Since then, Tobin and Marielle's combination of experience in healthcare, human resources and operations management has enabled them to grow the organization to 4 locations with 50+ providers across 6 specialties. Tobin and Marielle's passion and dedication to improving the lives of others, whether it be our patients, employees or physicians, is evident in every aspect of our organization and is articulated via our mission statement and core values.
    </div>
    <div class="diamond-frame frame-chair"></div>
    <div class="diamond img-chair" role="img" aria-label="Lawn chair and glass of wine on a dock at sunset over the lake"></div>
    <div class="plus" style="left:255px;top:462px;width:48px;height:48px"></div>
    <div class="plus" style="left:345px;top:546px;width:48px;height:48px"></div>
    <div class="plus" style="left:255px;top:640px;width:48px;height:48px"></div>
    <div class="corner corner--br"></div>
    <div class="page-tab">Pg 3</div>
  </div>
</section>

<section class="spread spread--three">
  <div class="page page--left">
    <div class="corner corner--tl"></div>
    <div class="brand--inside"><div class="brand-mark"><span class="brand-dot"></span><span class="brand">Bright Marrow Care</span></div></div>
    <div class="rule" style="top:124px"></div>
    <div class="mission-text">
      <h2 class="heading">Our Mission</h2>
      <div class="body">
        <p>Creating exceptional patient experiences for every patient, every time is not just our mission statement – it's a commitment to our patients. By creating a culture where we value the quality of care every patient receives first and foremost; that empowers our employees and providers to grow; and that treats every patient with compassion, dignity and respect, we deliver on our promise to our patients.</p>
      </div>
      <h2 class="heading" style="margin-top:16px">Our History</h2>
      <div class="body">
        <p>Our quest to deliver consistent access to care and to provide physicians with a healthy work/life balance began 9 years ago and is still the driving force behind our mission today. Bright Marrow Care started when a local pharmacist saw an opportunity to help his community that was struggling with a severe physician shortage and where thousands of people could not access care when or where they needed it. By offering physicians an operating model that gave them the ability to practice medicine without the stress of having to manage a business; a low overhead and the flexibility to practice medicine on their terms; and with the help of an experienced operations manager, he was immediately successful in attracting new physicians to the area when many others had failed. This idea became a reality when we opened our first location, Heron Bay Medical Clinic, in Lake Country, BC in 2016. A year later, our second location, Ridgeview Medical Clinic opened with the same vision and the same result.</p>
        <p>In May of 2020, during the height of the pandemic, our then operations manager, Tobin Raske, approached the owner of the clinics about selling the company to him and his wife Marielle. They saw an opportunity to help thousands more people secure access to care and to help physicians find a solution to the administrative burnout that was causing so many to leave family medicine at the time. Bright Marrow Care was born.</p>
        <p>In 2021, we opened our third location in the Pandosy neighborhood of Kelowna, the first location wearing the Bright Marrow Care name and also our first foray into multidisciplinary care with Sports Medicine and Family Practice providers working together in the same facility. Later that same year, the Northgate Medical team joined us and became our central Kelowna location, Bright Marrow Care – Springfield. After nearly a year of extensive renovations, the maternity care and family medicine group from Cedar Brook Family Medicine relocated and joined us at our Springfield location in early 2023.</p>
        <p>Today, Bright Marrow Care is comprised of more than 50 providers across 6 specialties and 4 locations. We are the largest, privately owned provider of primary care services in the Okanagan region and provide care to more than 80,000 residents.</p>
      </div>
    </div>
    <div class="corner corner--br"></div>
    <div class="page-tab">Pg 4</div>
  </div>
  <div class="page page--right">
    <div class="corner corner--tl"></div>
    <h2 class="heading" style="position:absolute;left:0;right:0;top:60px">Testimonials</h2>
    <div class="rule" style="top:84px"></div>
    <div class="testi-text body body--italic">
      <p>We believe that our employees are our greatest asset, and we strive to treat them with the same level of compassion, dignity, and respect that we provide to our patients. Employees' voices often speak the loudest about an organization's culture. To that end, we've highlighted genuine comments submitted by Bright Marrow Care employees &amp; providers that reflect our Mission, Values and commitment to them.</p>
      <div class="gap"></div>
      <p>I am a physician who has worked the past 47 years in Canada and the USA. One of my best experiences was to practise in Lake Country, BC at Bright Marrow Care. Their amazing team made our 4 years back in Canada a wonderful experience and their model allowed me to work as hard as I wanted, but also to take time off as desired. The overhead was reasonable and the work environment was great.</p>
      <p>The leadership at Bright Marrow Care were open to suggestions and made the transition into their office a pleasure. Lake Country/Kelowna is one of the best areas in Canada, with plenty of leisure activities year round. The only reason we returned to the US was my wife's desire to be back close to our children and grandchildren. If it was my choice I would still be there.</p>
      <p>During covid, the team transitioned to virtual medicine and then later to a hybrid model which I am sure will make anyone's practice adaptable. The reimbursement in BC is a great opportunity to adapt work to life balance and still get paid well. There is no better partner to work with in the Okanagan than Bright Marrow Care!</p>
      <div class="gap"></div>
      <p>I've had the pleasure of working with the team at Bright Marrow Care since 2016 as a part-time physician. During this time, I've served both as a family doctor and locum physician, primarily at the Heron Bay Medical Clinic in Lake Country, BC.</p>
      <p>Having previously co-owned three medical clinics in the Central Okanagan, I truly appreciate how Bright Marrow Care has removed the administrative burdens that come with clinical practice. This allows me to focus solely on what I was trained to do — providing patient care. The team fosters a welcoming and supportive environment for physicians, tailoring opportunities to align with each doctor's unique work goals. Management is approachable, responsive, and genuinely open to suggestions from both physicians and staff, creating a culture where collaboration thrives.</p>
      <p>The clinic's ClearChart EMR system is by far the most user-friendly I've encountered, further enhancing efficiency and workflow. I wholeheartedly recommend working with Bright Marrow Care. The supportive atmosphere, administrative relief, and innovative leadership make it my top choice for clinical practice — I wouldn't work anywhere else.</p>
    </div>
    <div class="plus" style="left:140px;top:578px;width:46px;height:46px"></div>
    <div class="plus" style="left:210px;top:612px;width:80px;height:80px"></div>
    <div class="plus" style="left:312px;top:578px;width:46px;height:46px"></div>
    <div class="corner corner--br"></div>
    <div class="page-tab">Pg 5</div>
  </div>
</section>

<section class="spread spread--four">
  <div class="page page--left">
    <div class="corner corner--tl"></div>
    <div class="brand--inside"><div class="brand-mark"><span class="brand-dot"></span><span class="brand">Bright Marrow Care</span></div></div>
    <div class="rule" style="top:122px"></div>
    <div class="region-text">
      <h2 class="heading">About Kelowna and The Okanagan Valley</h2>
      <div class="body">
        <p>If you are considering working or living in the Kelowna area, take a look at all that the Okanagan Valley has to offer.</p>
        <p>Nestled in the heart of British Columbia, the Okanagan Valley offers a lifestyle like no other. Wake up to stunning lake views, hike through breathtaking mountain trails, and spend your days exploring world-class vineyards, sandy beaches, and outdoor adventures. Whether you're skiing in winter, boating in summer, or enjoying vibrant arts and local culture, the Okanagan Valley is a place to live life to the fullest. Come for the natural beauty, stay for the laid-back lifestyle!</p>
        <p>Kelowna has experienced a population growth of 14% since 2016, making it the fastest growing metropolitan area in Canada. With over 165,000 residents, and a median age of 42, it is also the 6th largest, and one of the youngest cities in the province of British Columbia. Situated in the heart of the Okanagan Valley, Kelowna is surrounded by mountains, lakes and vineyards where residents embrace outdoor adventures and an active lifestyle all year long. The city is also an economic powerhouse, home to robust traditional sectors like agriculture and construction, and burgeoning new sectors such as information technology.</p>
      </div>
      <h2 class="heading" style="margin-top:10px">Healthcare – Climate and Outdoor Recreation</h2>
      <div class="body">
        <p>The Okanagan Valley offers an abundance of outdoor activities ranging from water sports in the summer to skiing in the winter, as well as hiking, biking, and opportunities for relaxation and nature immersion. It's a great place for year-round outdoor adventure, including 35 provincial parks, more than 100 lakes, same-day access to 5 world class ski resorts and 186 wineries.</p>
        <p>With over 2,000 hours of sunshine a year, the Okanagan Valley boasts one of the best climates in Canada. Enjoy warm, dry summers ideal for outdoor activities, relaxing at lakeside beaches, and exploring vineyards. Winters bring a beautiful balance of mild temperatures and snowy mountain peaks — famous for their champagne powder. Whether you're a sun-seeker or snow lover, the Okanagan offers the ideal climate year-round with average daytime high temperatures ranging from 2°C (36°F) in January to 28°C (82°F) in July.</p>
      </div>
      <h2 class="heading" style="margin-top:10px">Things to do – Attractions</h2>
      <div class="todo">
        <span>• Skyline Aviation Centre</span><span>• Wallaby Hollow Farm</span>
        <span>• Valley Discovery Centre</span><span>• Lakeside Rail Trail</span>
        <span>• Canyon Trestle Trail</span><span>• Okanagan Lake</span>
        <span>• Splashpoint Aquatic Centre</span><span>• Lakeview Place Arena and Events Centre</span>
      </div>
    </div>
    <div class="corner corner--br"></div>
    <div class="page-tab">Pg 6</div>
  </div>
  <div class="page page--right">
    <div class="corner corner--tl"></div>
    <div class="lists">
      <div class="list-block" style="left:56px;top:108px">
        <div class="plus plus--teal"></div>
        <h3>Parks</h3>
        <ul><li>Bruin Creek Provincial Park</li><li>Finlay Point Provincial Park</li><li>Highpeak National Park</li><li>Glacierline National Park</li><li>City Park</li><li>Willow Creek Regional Park</li><li>Summit Ridge Park</li></ul>
      </div>
      <div class="list-block" style="left:276px;top:104px">
        <div class="plus plus--teal"></div>
        <h3>Arts</h3>
        <ul><li>Valley Symphony Orchestra</li><li>Lakeside Art Gallery</li><li>Harbour Centre for the Arts</li><li>Stagelight Dinner Theatre</li><li>Valley Heritage Museum</li><li>Vine and Orchard Museum</li></ul>
      </div>
      <div class="list-block" style="left:56px;top:232px">
        <div class="plus plus--teal"></div>
        <h3>Higher Education</h3>
        <ul><li>Interior Pacific University</li><li>Valley Community College</li><li>Lakeshore Institute of Design</li><li>Westcoast Technical Institute</li></ul>
      </div>
      <div class="list-block" style="left:276px;top:232px">
        <div class="plus plus--teal"></div>
        <h3>Events</h3>
        <ul><li>Lakeshore Rock Festival</li><li>Open Water Lake Swim</li><li>Summer Diamond Festival</li><li>Valley Harvest Wine Festival</li><li>Ridgetop Hill Climb</li></ul>
      </div>
      <div class="list-block" style="left:56px;top:336px">
        <div class="plus plus--teal"></div>
        <h3>Sports</h3>
        <ul><li>Lakeside Comets Hockey Team</li><li>Lakeside Kestrels Baseball</li><li>Lakeside Blaze Football</li><li>Lakeside Ridgebacks Lacrosse</li></ul>
      </div>
    </div>
    <div class="diamond-frame frame-ski"></div>
    <div class="diamond img-ski" role="img" aria-label="Skiers riding a chairlift through snow-covered trees"></div>
    <div class="corner corner--br"></div>
    <div class="page-tab">Pg 7</div>
  </div>
</section>

</body>
</html>
```